QR-482 Horizons, LLC business cards
Personal Fitness Training
Professional
QR 482 Horizons, LLC
Fitness Solutions
based out of Miami but want to train internationally over the net
bellamorvain@qr482.net
www.qr482.net
K20000047153
I would also like to list my bellamorvain@zentmail.net email
I will be based out of the Miami area but do not have an exact location for the address.
Contact for your Free Fitness Assessment
415 263 9071 or bellamorvain@qr482.net

```html
<!DOCTYPE html>
<html lang="en">
<head>
<meta charset="utf-8">
<title>QR-482 Horizons, LLC — Business Cards</title>
<link href="https://fonts.googleapis.com/css2?family=Open+Sans:wght@400;700&display=swap" rel="stylesheet">
<style>
  :root {
    --page: #ffffff;
    --frame: #c9c9c9;
    --card-edge: #bdbdbd;
    --ink: #1d1d1d;
    --brand-blue: #2aa7e0;
    --silver-light: #f3f3f3;
    --silver-mid: #d8d8d8;
    --silver-dark: #b2b2b2;
  }
  * { box-sizing: border-box; margin: 0; padding: 0; }
  html, body { width: 1200px; height: 403px; overflow: hidden; background: var(--page); }
  body { font-family: "Open Sans", Arial, sans-serif; color: var(--ink); position: relative; }

  .presentation-frame {
    position: absolute; left: 6px; top: 6px; width: 1188px; height: 391px;
    border: 2px solid var(--frame); border-radius: 10px;
  }
  .card {
    position: absolute; top: 34px; width: 562px; height: 332px;
    border: 1px solid var(--card-edge); overflow: hidden;
  }
  .card--front { left: 28px; background: #fff; }
  .card--back {
    left: 608px;
    background: radial-gradient(ellipse at 50% 42%, var(--silver-light) 0%, var(--silver-mid) 60%, var(--silver-dark) 100%);
  }

  .wordmark {
    position: absolute; left: 0; right: 0; text-align: center;
    font-size: 34px; line-height: 40px; font-weight: 400; color: var(--ink);
  }
  .card--front .wordmark { top: 61px; }
  .card--back .wordmark { top: 117px; }

  .company { position: absolute; left: 0; right: 0; top: 138px; text-align: center; font-size: 12px; line-height: 22px; }
  .company__name { color: var(--brand-blue); }

  .contact-band {
    position: absolute; left: 0; right: 0; top: 203px; bottom: 0;
    background: linear-gradient(180deg, var(--silver-dark) 0%, var(--silver-mid) 45%, var(--silver-light) 100%);
  }
  .contact-list {
    position: absolute; left: 0; top: 25px; display: grid;
    grid-template-columns: 254px auto; column-gap: 12px;
    font-size: 15px; line-height: 22px;
  }
  .contact-list dt { text-align: right; font-weight: 700; }
  .contact-list dd { font-weight: 400; }

  .back-cta {
    position: absolute; left: 0; right: 0; top: 247px; text-align: center;
    font-size: 12px; line-height: 18px; font-weight: 700;
  }
  .back-divider {
    position: absolute; left: 40px; right: 40px; top: 270px; height: 1px;
    background: linear-gradient(90deg, transparent, rgba(255,255,255,.9), transparent);
  }
  .back-contact {
    position: absolute; left: 0; right: 0; top: 279px; text-align: center;
    font-size: 12px; line-height: 18px;
  }
</style>
</head>
<body>
  <div class="presentation-frame"></div>

  <section class="card card--front" aria-label="Card front">
    <p class="wordmark">QR-482 Horizons</p>
    <div class="company">
      <p class="company__name">QR 482 Horizons, LLC</p>
      <p class="company__tagline">Personal Fitness Solutions</p>
    </div>
    <div class="contact-band">
      <dl class="contact-list">
        <dt>Phone</dt><dd>415 263 9071</dd>
        <dt>Email</dt><dd>bellamorvain@qr482.net</dd>
        <dt>Web</dt><dd>www.qr482.net</dd>
        <dt>License No</dt><dd>K20000047153</dd>
      </dl>
    </div>
  </section>

  <section class="card card--back" aria-label="Card back">
    <p class="wordmark">QR-482 Horizons</p>
    <p class="back-cta">Contact for your Free Fitness Assessment</p>
    <div class="back-divider"></div>
    <p class="back-contact">415 263 9071 , bellamorvain@qr482.net</p>
  </section>
</body>
</html>
```